CATALOGUE OF DIAMOND RINGS NEEDED

I have approximately 200 images that need to be designed in a way to be a catalogue. I would firstly like to see a page with about 30 images on it. You can find the images by going to this link; http://velmontrix.com/collection.php?cid=28&tid=33&lang=&page=2 (you may pick any 30 images you like). and then if I like your design of this page, I will invite you through briefharbor to put together the other 6 or 7 pages in a similar way using the other images from this site, and some others. The amount I am paying here, will only be for one page, and then you will be paid more for doing the other pages. you may simply number the products 1,2,3 but have a list on the side of the page that will allow me or you to input details about the item. for example KMT8204 will require information such as $1300. 26 Round Diamonds totaling 0.40 carats.

Colors
86acd3
3377b5
0355a3
cfdfed
86cae6
34a6d7
0493ce
cee9f5

Requirements
Must have
• I really like the look of this catalogue, but it doesn't have to be anything like this. I am open to many different ideas.
• http://ab.pkl.co.za/photos/ballroom/1.jpg

```html
<!DOCTYPE html>
<html lang="en">
<head>
<meta charset="utf-8">
<title>Solmara Jewellery – Ring Catalogue</title>
<link rel="stylesheet" href="https://fonts.googleapis.com/css2?family=Rokkitt:wght@400;700&display=swap">
<style>
  :root {
    --frame: #000000;
    --deep-blue: #0355a3;
    --mid-blue: #3377b5;
    --bright-blue: #0493ce;
    --sky-blue: #34a6d7;
    --pale-blue: #cfdfed;
    --ice-blue: #cee9f5;
    --text-light: #cfdfed;
    --price: #ffffff;
    --silver-hi: #f4f6f8;
    --silver-lo: #9aa6b2;
  }
  html, body { margin: 0; padding: 0; width: 947px; height: 1200px; overflow: hidden; background: var(--frame); }
  .canvas {
    position: relative; width: 900px; height: 1140px;
    transform: scale(1.05222, 1.05263); transform-origin: 0 0;
    font-family: "Rokkitt", Georgia, serif;
  }
  .page { position: absolute; left: 42px; top: 42px; width: 816px; height: 1056px; overflow: hidden; }
  .page-backdrop { position: absolute; inset: 0; width: 100%; height: 100%; }
  .section-label {
    position: absolute; margin: 0; font-weight: 400; font-size: 10.5px;
    letter-spacing: 0.5px; color: var(--text-light);
  }
  .ring {
    position: absolute; border-radius: 46% 46% 50% 50%;
    background: radial-gradient(ellipse at 40% 35%, var(--silver-hi) 0%, #d8dee5 45%, var(--silver-lo) 100%);
    box-shadow: 0 6px 8px rgba(0, 20, 60, 0.35);
  }
  .ring.feature { background: radial-gradient(ellipse at 45% 35%, #f8e7a0 0%, #e9d98a 18%, #e6eaee 40%, var(--silver-lo) 100%); }
  .spec-list {
    position: absolute; margin: 0; padding: 0; list-style: none;
    font-size: 8.6px; line-height: 15.6px; color: var(--text-light); white-space: nowrap;
  }
  .spec-list .price { font-weight: 700; color: var(--price); }
  .brand {
    position: absolute; right: 52px; bottom: 50px;
    display: flex; align-items: center; gap: 8px;
    color: #ffffff; font-size: 12px;
  }
  .brand-dot { width: 12px; height: 12px; border-radius: 50%; background: #ffffff; }
</style>
</head>
<body>
<div class="canvas">
  <div class="page">
    <svg class="page-backdrop" viewBox="0 0 816 1056" preserveAspectRatio="none" aria-hidden="true">
      <defs>
        <linearGradient id="bg" x1="0" y1="0" x2="1" y2="1">
          <stop offset="0" stop-color="#0a62ae"/>
          <stop offset="1" stop-color="#03479a"/>
        </linearGradient>
        <radialGradient id="glow" cx="0.1" cy="0.1" r="0.9">
          <stop offset="0" stop-color="#2c8fd3"/>
          <stop offset="1" stop-color="#0355a3" stop-opacity="0"/>
        </radialGradient>
        <linearGradient id="sweep" x1="0" y1="0" x2="1" y2="0">
          <stop offset="0" stop-color="#34a6d7"/>
          <stop offset="0.6" stop-color="#0493ce"/>
          <stop offset="1" stop-color="#0355a3"/>
        </linearGradient>
      </defs>
      <rect width="816" height="1056" fill="url(#bg)"/>
      <path d="M0 0 H260 C120 120 20 320 0 560 Z" fill="url(#glow)"/>
      <path d="M0 0 H250 C110 130 10 340 0 600 Z" fill="none" stroke="#3a9ad8" stroke-opacity="0.5" stroke-width="2"/>
      <path d="M0 900 C200 1000 520 1010 816 940 V1056 H0 Z" fill="url(#sweep)" opacity="0.85"/>
      <path d="M0 900 C200 1000 520 1010 816 940" fill="none" stroke="#86cae6" stroke-opacity="0.5" stroke-width="1.5"/>
    </svg>
  </div>

  <!-- Section A -->
  <h2 class="section-label" style="left:127px;top:148px">A &nbsp;|&nbsp; 1 to 8</h2>
  <div class="ring" role="img" aria-label="Ring 1, halo setting" style="left:117px;top:182px;width:66px;height:62px"></div>
  <div class="ring" role="img" aria-label="Ring 2, oval halo setting, featured" style="left:178px;top:178px;width:125px;height:166px"></div>
  <div class="ring" role="img" aria-label="Ring 3, halo setting" style="left:312px;top:178px;width:68px;height:66px"></div>
  <div class="ring" role="img" aria-label="Ring 4, solitaire mount" style="left:395px;top:186px;width:80px;height:56px"></div>
  <div class="ring feature" role="img" aria-label="Ring 5, yellow diamond halo" style="left:478px;top:180px;width:78px;height:62px"></div>
  <div class="ring" role="img" aria-label="Ring 6, solitaire mount" style="left:557px;top:186px;width:80px;height:56px"></div>
  <div class="ring" role="img" aria-label="Ring 7, halo setting" style="left:639px;top:178px;width:80px;height:64px"></div>
  <div class="ring" role="img" aria-label="Ring 8, halo setting" style="left:722px;top:180px;width:78px;height:64px"></div>
  <ul class="spec-list" style="left:340px;top:258px">
    <li>1. KMT8204 &nbsp;|&nbsp; 26 Round Diamonds &nbsp;|&nbsp; 0.40 carats &nbsp;|&nbsp; <span class="price">$1300</span></li>
    <li>1. KMT8204 &nbsp;|&nbsp; 26 Round Diamonds &nbsp;|&nbsp; 0.40 carats &nbsp;|&nbsp; <span class="price">$1300</span></li>
    <li>1. KMT8204 &nbsp;|&nbsp; 26 Round Diamonds &nbsp;|&nbsp; 0.40 carats &nbsp;|&nbsp; <span class="price">$1300</span></li>
    <li>1. KMT8204 &nbsp;|&nbsp; 26 Round Diamonds &nbsp;|&nbsp; 0.40 carats &nbsp;|&nbsp; <span class="price">$1300</span></li>
  </ul>
  <ul class="spec-list" style="left:580px;top:258px">
    <li>1. KMT8204 &nbsp;|&nbsp; 26 Round Diamonds &nbsp;|&nbsp; 0.40 carats &nbsp;|&nbsp; <span class="price">$1300</span></li>
    <li>1. KMT8204 &nbsp;|&nbsp; 26 Round Diamonds &nbsp;|&nbsp; 0.40 carats &nbsp;|&nbsp; <span class="price">$1300</span></li>
    <li>1. KMT8204 &nbsp;|&nbsp; 26 Round Diamonds &nbsp;|&nbsp; 0.40 carats &nbsp;|&nbsp; <span class="price">$1300</span></li>
    <li>1. KMT8204 &nbsp;|&nbsp; 26 Round Diamonds &nbsp;|&nbsp; 0.40 carats &nbsp;|&nbsp; <span class="price">$1300</span></li>
  </ul>

  <!-- Section B -->
  <h2 class="section-label" style="left:127px;top:360px">B &nbsp;|&nbsp; 1 to 8</h2>
  <div class="ring" role="img" aria-label="Ring 1, halo setting" style="left:117px;top:386px;width:66px;height:64px"></div>
  <div class="ring" role="img" aria-label="Ring 2, halo setting" style="left:185px;top:380px;width:82px;height:70px"></div>
  <div class="ring" role="img" aria-label="Ring 3, solitaire mount" style="left:270px;top:388px;width:82px;height:60px"></div>
  <div class="ring feature" role="img" aria-label="Ring 4, yellow diamond halo" style="left:354px;top:382px;width:78px;height:68px"></div>
  <div class="ring" role="img" aria-label="Ring 5, halo setting" style="left:436px;top:386px;width:72px;height:64px"></div>
  <div class="ring" role="img" aria-label="Ring 6, solitaire mount" style="left:512px;top:388px;width:82px;height:60px"></div>
  <div class="ring" role="img" aria-label="Ring 7, round halo setting, featured" style="left:596px;top:396px;width:124px;height:134px"></div>
  <div class="ring" role="img" aria-label="Ring 8, halo setting" style="left:722px;top:388px;width:68px;height:62px"></div>
  <ul class="spec-list" style="left:117px;top:469px">
    <li>1. KMT8204 &nbsp;|&nbsp; 26 Round Diamonds &nbsp;|&nbsp; 0.40 carats &nbsp;|&nbsp; <span class="price">$1300</span></li>
    <li>1. KMT8204 &nbsp;|&nbsp; 26 Round Diamonds &nbsp;|&nbsp; 0.40 carats &nbsp;|&nbsp; <span class="price">$1300</span></li>
    <li>1. KMT8204 &nbsp;|&nbsp; 26 Round Diamonds &nbsp;|&nbsp; 0.40 carats &nbsp;|&nbsp; <span class="price">$1300</span></li>
    <li>1. KMT8204 &nbsp;|&nbsp; 26 Round Diamonds &nbsp;|&nbsp; 0.40 carats &nbsp;|&nbsp; <span class="price">$1300</span></li>
  </ul>
  <ul class="spec-list" style="left:353px;top:469px">
    <li>1. KMT8204 &nbsp;|&nbsp; 26 Round Diamonds &nbsp;|&nbsp; 0.40 carats &nbsp;|&nbsp; <span class="price">$1300</span></li>
    <li>1. KMT8204 &nbsp;|&nbsp; 26 Round Diamonds &nbsp;|&nbsp; 0.40 carats &nbsp;|&nbsp; <span class="price">$1300</span></li>
    <li>1. KMT8204 &nbsp;|&nbsp; 26 Round Diamonds &nbsp;|&nbsp; 0.40 carats &nbsp;|&nbsp; <span class="price">$1300</span></li>
    <li>1. KMT8204 &nbsp;|&nbsp; 26 Round Diamonds &nbsp;|&nbsp; 0.40 carats &nbsp;|&nbsp; <span class="price">$1300</span></li>
  </ul>

  <!-- Section C -->
  <h2 class="section-label" style="left:127px;top:564px">C &nbsp;|&nbsp; 1 to 8</h2>
  <div class="ring" role="img" aria-label="Ring 1, halo setting" style="left:108px;top:586px;width:84px;height:74px"></div>
  <div class="ring feature" role="img" aria-label="Ring 2, yellow cushion diamond halo, featured" style="left:175px;top:602px;width:145px;height:138px"></div>
  <div class="ring" role="img" aria-label="Ring 3, halo setting" style="left:322px;top:596px;width:66px;height:66px"></div>
  <div class="ring" role="img" aria-label="Ring 4, solitaire mount" style="left:390px;top:598px;width:82px;height:62px"></div>
  <div class="ring feature" role="img" aria-label="Ring 5, yellow diamond halo" style="left:474px;top:594px;width:82px;height:66px"></div>
  <div class="ring" role="img" aria-label="Ring 6, solitaire mount" style="left:558px;top:598px;width:82px;height:62px"></div>
  <div class="ring" role="img" aria-label="Ring 7, halo setting" style="left:642px;top:590px;width:82px;height:72px"></div>
  <div class="ring" role="img" aria-label="Ring 8, halo setting" style="left:728px;top:596px;width:68px;height:66px"></div>
  <ul class="spec-list" style="left:348px;top:680px">
    <li>1. KMT8204 &nbsp;|&nbsp; 26 Round Diamonds &nbsp;|&nbsp; 0.40 carats &nbsp;|&nbsp; <span class="price">$1300</span></li>
    <li>1. KMT8204 &nbsp;|&nbsp; 26 Round Diamonds &nbsp;|&nbsp; 0.40 carats &nbsp;|&nbsp; <span class="price">$1300</span></li>
    <li>1. KMT8204 &nbsp;|&nbsp; 26 Round Diamonds &nbsp;|&nbsp; 0.40 carats &nbsp;|&nbsp; <span class="price">$1300</span></li>
    <li>1. KMT8204 &nbsp;|&nbsp; 26 Round Diamonds &nbsp;|&nbsp; 0.40 carats &nbsp;|&nbsp; <span class="price">$1300</span></li>
  </ul>
  <ul class="spec-list" style="left:587px;top:680px">
    <li>1. KMT8204 &nbsp;|&nbsp; 26 Round Diamonds &nbsp;|&nbsp; 0.40 carats &nbsp;|&nbsp; <span class="price">$1300</span></li>
    <li>1. KMT8204 &nbsp;|&nbsp; 26 Round Diamonds &nbsp;|&nbsp; 0.40 carats &nbsp;|&nbsp; <span class="price">$1300</span></li>
    <li>1. KMT8204 &nbsp;|&nbsp; 26 Round Diamonds &nbsp;|&nbsp; 0.40 carats &nbsp;|&nbsp; <span class="price">$1300</span></li>
    <li>1. KMT8204 &nbsp;|&nbsp; 26 Round Diamonds &nbsp;|&nbsp; 0.40 carats &nbsp;|&nbsp; <span class="price">$1300</span></li>
  </ul>

  <!-- Section D -->
  <h2 class="section-label" style="left:127px;top:785px">D &nbsp;|&nbsp; 1 to 8</h2>
  <div class="ring" role="img" aria-label="Ring 1, halo setting" style="left:105px;top:812px;width:66px;height:66px"></div>
  <div class="ring" role="img" aria-label="Ring 2, halo setting" style="left:172px;top:808px;width:84px;height:70px"></div>
  <div class="ring" role="img" aria-label="Ring 3, solitaire mount" style="left:257px;top:812px;width:82px;height:64px"></div>
  <div class="ring feature" role="img" aria-label="Ring 4, yellow diamond halo" style="left:340px;top:808px;width:80px;height:70px"></div>
  <div class="ring" role="img" aria-label="Ring 5, solitaire mount" style="left:422px;top:812px;width:82px;height:64px"></div>
  <div class="ring" role="img" aria-label="Ring 6, halo setting" style="left:506px;top:808px;width:84px;height:70px"></div>
  <div class="ring" role="img" aria-label="Ring 7, round halo setting, featured" style="left:592px;top:812px;width:98px;height:134px"></div>
  <div class="ring" role="img" aria-label="Ring 8, solitaire mount" style="left:706px;top:814px;width:84px;height:62px"></div>
  <ul class="spec-list" style="left:103px;top:896px">
    <li>1. KMT8204 &nbsp;|&nbsp; 26 Round Diamonds &nbsp;|&nbsp; 0.40 carats &nbsp;|&nbsp; <span class="price">$1300</span></li>
    <li>1. KMT8204 &nbsp;|&nbsp; 26 Round Diamonds &nbsp;|&nbsp; 0.40 carats &nbsp;|&nbsp; <span class="price">$1300</span></li>
    <li>1. KMT8204 &nbsp;|&nbsp; 26 Round Diamonds &nbsp;|&nbsp; 0.40 carats &nbsp;|&nbsp; <span class="price">$1300</span></li>
    <li>1. KMT8204 &nbsp;|&nbsp; 26 Round Diamonds &nbsp;|&nbsp; 0.40 carats &nbsp;|&nbsp; <span class="price">$1300</span></li>
  </ul>
  <ul class="spec-list" style="left:340px;top:896px">
    <li>1. KMT8204 &nbsp;|&nbsp; 26 Round Diamonds &nbsp;|&nbsp; 0.40 carats &nbsp;|&nbsp; <span class="price">$1300</span></li>
    <li>1. KMT8204 &nbsp;|&nbsp; 26 Round Diamonds &nbsp;|&nbsp; 0.40 carats &nbsp;|&nbsp; <span class="price">$1300</span></li>
    <li>1. KMT8204 &nbsp;|&nbsp; 26 Round Diamonds &nbsp;|&nbsp; 0.40 carats &nbsp;|&nbsp; <span class="price">$1300</span></li>
    <li>1. KMT8204 &nbsp;|&nbsp; 26 Round Diamonds &nbsp;|&nbsp; 0.40 carats &nbsp;|&nbsp; <span class="price">$1300</span></li>
  </ul>

  <div class="brand">
    <span class="brand-dot"></span>
    <span class="brand-name">Solmara Jewellery</span>
  </div>
</div>
</body>
</html>
```